Event flyer for Sunday night Youth Group

Need a 4 x 6 or 5 x 7 flyer for a new youth group starting on April 14. The youth group is for students in middle school and high school so it needs to look fun and cool, but not childish. I prefer it not to include pictures of people unless it's so obscure you can't really see their faces. I've uploaded some pictures of flyers I like. I've also attached a couple versions of our logo to use on the flyer.
Information the flyer needs to include:
Youth Group
Sundays, 6-8pm (beginning April 14)
Location: Wexlander's - 4182 Quillon Ridge Ave N, Marlowe, 97158
There will be dinner, games, friends, and a message.
Target Market(s)
Youth ages 13-18
Industry/Entity Type
Church
Colors
Look and feel

```html
<!DOCTYPE html>
<html lang="en">
<head>
<meta charset="utf-8">
<title>Youth Group — Sundays</title>
<link href="https://fonts.googleapis.com/css2?family=Anton&family=Bebas+Neue&family=Montserrat:wght@400;500;600&display=swap" rel="stylesheet">
<style>
  :root{
    --bg:#2d1445;
    --paper:#f2f2f2;
    --violet:#5b2aa6;
    --magenta:#c4246c;
    --blue:#3a90d0;
    --teal:#2aa58e;
    --pink:#ef4a9e;
    --red:#ea3461;
    --orange:#ee8d3a;
  }
  *{margin:0;padding:0;box-sizing:border-box}
  html,body{width:848px;height:1200px;overflow:hidden;background:var(--bg)}
  .flyer{position:relative;width:848px;height:1200px;background:var(--bg);overflow:hidden;font-family:'Montserrat',sans-serif;color:var(--paper)}
  .backdrop{position:absolute;inset:0}
  .brand{position:absolute;left:0;width:848px;top:150px;text-align:center;font-family:'Montserrat',sans-serif;font-weight:500;color:var(--paper)}
  .brand-mark{display:block;width:22px;height:22px;margin:0 auto 14px;background:var(--paper)}
  .brand-name{display:block;font-size:30px;letter-spacing:0.01em;line-height:1}
  .brand-sub{display:block;font-size:14px;letter-spacing:0.42em;margin-top:6px;padding-left:0.42em}
  .side-tag{position:absolute;left:140px;top:721px;transform-origin:0 0;transform:rotate(-90deg);font-size:12.5px;font-weight:500;letter-spacing:0.3em;white-space:nowrap;width:423px}
  .schedule{position:absolute;left:264px;top:773px;font-family:'Bebas Neue',sans-serif;line-height:0.9}
  .schedule .day{display:block;font-size:75px;letter-spacing:0.03em;color:var(--blue)}
  .schedule .time{display:block;font-size:75px;letter-spacing:0.04em;color:var(--paper);margin-top:-4px}
  .start{position:absolute;left:566px;top:748px;width:180px;text-align:center;font-family:'Bebas Neue',sans-serif;font-size:47px;line-height:0.95;color:var(--paper)}
  .address{position:absolute;left:266px;top:952px;font-size:22px;font-weight:500;line-height:32px;letter-spacing:0.02em;font-style:normal}
  .tagline{position:absolute;left:134px;top:1067px;font-family:'Bebas Neue',sans-serif;font-size:31px;letter-spacing:0.12em;white-space:nowrap}
  .tagline .games{color:var(--red)}
  .tagline .friends{color:var(--orange)}
  .tagline .message{color:var(--blue)}
</style>
</head>
<body>
<main class="flyer">
  <svg class="backdrop" width="848" height="1200" viewBox="0 0 848 1200" aria-hidden="true">
    <defs>
      <linearGradient id="orbMain" x1="0.15" y1="0.85" x2="0.85" y2="0.15">
        <stop offset="0" stop-color="#3b1a66"/>
        <stop offset="0.45" stop-color="#5a27a2"/>
        <stop offset="1" stop-color="#cc2467"/>
      </linearGradient>
      <linearGradient id="orbLeft" x1="0" y1="0.8" x2="1" y2="0">
        <stop offset="0" stop-color="#4a1f86"/>
        <stop offset="1" stop-color="#9a2068"/>
      </linearGradient>
      <linearGradient id="orbTeal" x1="0.1" y1="0.9" x2="0.9" y2="0.1">
        <stop offset="0" stop-color="#3a1a58"/>
        <stop offset="0.45" stop-color="#2a9e8a"/>
        <stop offset="1" stop-color="#3a8fde"/>
      </linearGradient>
      <linearGradient id="orbSmall" x1="0" y1="1" x2="1" y2="0">
        <stop offset="0" stop-color="#3d1b70"/>
        <stop offset="1" stop-color="#8a2070"/>
      </linearGradient>
    </defs>
    <circle cx="171" cy="268" r="138" fill="url(#orbLeft)" opacity="0.85"/>
    <circle cx="444" cy="523" r="298" fill="url(#orbMain)" opacity="0.92"/>
    <circle cx="657" cy="313" r="41" fill="url(#orbSmall)" opacity="0.7"/>
    <circle cx="222" cy="496" r="22" fill="url(#orbSmall)" opacity="0.7"/>
    <circle cx="208" cy="726" r="36" fill="url(#orbSmall)" opacity="0.7"/>
    <circle cx="657" cy="785" r="127" fill="url(#orbTeal)" opacity="0.88"/>

    <g class="dot-grid" fill="#f2f2f2">
      <circle cx="123" cy="168" r="1.8"/><circle cx="133" cy="168" r="1.8"/><circle cx="144" cy="168" r="1.8"/>
      <circle cx="123" cy="180" r="1.8"/><circle cx="133" cy="180" r="1.8"/><circle cx="144" cy="180" r="1.8"/>
      <circle cx="123" cy="193" r="1.8"/><circle cx="133" cy="193" r="1.8"/><circle cx="144" cy="193" r="1.8"/>
      <circle cx="123" cy="205" r="1.8"/><circle cx="133" cy="205" r="1.8"/><circle cx="144" cy="205" r="1.8"/>
      <circle cx="133" cy="218" r="1.8"/><circle cx="144" cy="218" r="1.8"/>
      <circle cx="133" cy="230" r="1.8"/><circle cx="144" cy="230" r="1.8"/>
      <circle cx="133" cy="243" r="1.8"/><circle cx="144" cy="243" r="1.8"/>
      <circle cx="133" cy="255" r="1.8"/><circle cx="144" cy="255" r="1.8"/>
      <circle cx="133" cy="268" r="1.8"/><circle cx="144" cy="268" r="1.8"/>
    </g>
    <g class="dot-grid" fill="#f2f2f2">
      <circle cx="717" cy="1021" r="1.8"/><circle cx="728" cy="1021" r="1.8"/><circle cx="738" cy="1021" r="1.8"/>
      <circle cx="717" cy="1033" r="1.8"/><circle cx="728" cy="1033" r="1.8"/><circle cx="738" cy="1033" r="1.8"/>
      <circle cx="717" cy="1046" r="1.8"/><circle cx="728" cy="1046" r="1.8"/><circle cx="738" cy="1046" r="1.8"/>
      <circle cx="717" cy="1058" r="1.8"/><circle cx="728" cy="1058" r="1.8"/><circle cx="738" cy="1058" r="1.8"/>
      <circle cx="728" cy="1070" r="1.8"/><circle cx="738" cy="1070" r="1.8"/>
      <circle cx="728" cy="1083" r="1.8"/><circle cx="738" cy="1083" r="1.8"/>
      <circle cx="728" cy="1095" r="1.8"/><circle cx="738" cy="1095" r="1.8"/>
      <circle cx="728" cy="1107" r="1.8"/><circle cx="738" cy="1107" r="1.8"/>
      <circle cx="728" cy="1119" r="1.8"/><circle cx="738" cy="1119" r="1.8"/>
    </g>

    <g class="title-rules" fill="#f2f2f2">
      <rect x="269" y="301" width="339" height="8"/>
      <rect x="269" y="717" width="339" height="8"/>
    </g>

    <g class="dot-stack">
      <circle cx="641" cy="449" r="12.5" fill="#ef4a9e"/>
      <circle cx="641" cy="487" r="12.5" fill="#ea3461"/>
      <circle cx="641" cy="524" r="12.5" fill="#ee8d3a"/>
      <circle cx="225" cy="793" r="14" fill="#ef4a9e"/>
      <circle cx="225" cy="835" r="14" fill="#ea3461"/>
      <circle cx="225" cy="877" r="14" fill="#ee8d3a"/>
    </g>

    <g class="title" fill="#f2f2f2" font-family="Anton, sans-serif">
      <text x="268" y="493" font-size="180" textLength="339" lengthAdjust="spacingAndGlyphs">YOUTH</text>
      <text x="268" y="675" font-size="180" textLength="337" lengthAdjust="spacingAndGlyphs">GROUP</text>
    </g>

    <g class="pin-icon" fill="none" stroke="#e8345f" stroke-width="3">
      <path d="M226 1006 L212 985 A16 16 0 1 1 240 985 Z" fill="#e8345f" stroke="none"/>
      <circle cx="226" cy="974" r="5" fill="#2d1445" stroke="none"/>
      <ellipse cx="226" cy="993" rx="17" ry="6"/>
    </g>
  </svg>

  <header class="brand">
    <span class="brand-mark"></span>
    <span class="brand-name">WAYPOINT</span>
    <span class="brand-sub">FELLOWSHIP</span>
  </header>

  <p class="side-tag">DINNER, GAMES, FRIENDS, AND A MESSAGE</p>

  <p class="schedule">
    <span class="day">SUNDAYS</span>
    <span class="time">6PM-8PM</span>
  </p>

  <p class="start">BEGINNING<br>APRIL 14</p>

  <address class="address">
    WEXLANDER'S - 4182 QUILLON<br>RIDGE AVE N, MARLOWE, 97158
  </address>

  <p class="tagline">DINNER, <span class="games">GAMES</span>, <span class="friends">FRIENDS</span>, AND <span class="message">A MESSAGE</span></p>
</main>
</body>
</html>
```